Design a Unique and Eye-Catching Necklace Card for Wendaray's New Brightwell Line

Attention all creative minds from around the world! Wendaray, a company known for its free-spirited and bohemian chic vibe, is proud to announce a new design contest. We are inviting you to create a dynamic and unique necklace card for our upcoming Brightwell line.

Our new Brightwell line comprises 12-20 unique necklace combinations. Each necklace features different stones, each with its own healing properties and associated zodiac sign. We are looking for a template that can be easily modified to change the names of the stones, zodiac sign, and the colors to match the specific stones on each necklace.

The card should be 3 x 4,
It should include the names of the stones, the associated zodiac sign (if applicable), a few words about the healing properties of the stones, and a captivating graphic that represents the colors of the stones.

Our goal is to delight our customers with packaging as unique as the necklaces themselves. The necklace should be the focal point, but the text and graphic on the card should also draw the eye.

Please note that our target audience includes mid-priced boutiques across the country and festival-goers in Colorado. Your design should reflect the unique taste and free spirit of our clientele.

We are excited to see your creativity shine in this project. If there are any points that need clarification, please do not hesitate to ask. We look forward to your participation in bringing the Brightwell line to life!
https://www.draftnook.example/board/KQ7mPzR2tLw/edit

https://www.draftnook.example/board/VJ3nHsX8qYb/edit
I want to use the flowing watercolor and have it change with each necklace color.
Use the necklaces below. Incorporate the zodiac symbol as is shown below.

Examples of other cards in our collection

The Little Pebble Pendant: https://www.draftnook.example/board/TB5wGdM4cRu/edit

Other examples of necklace cards I like:

https://www.craftbazaro.example/item/731905284/green-stone-pendant

https://www.craftbazaro.example/item/462918037/birthstone-pendant-green

https://www.craftbazaro.example/item/2907315628/crystal-bead-bracelets

https://www.craftbazaro.example/item/3816402795/dark-stone-guard-pendant

Target Market(s)

Women aged 25-50 with a spiritual, hippy, bohemain, yoga vibe.

Industry/Entity Type

Handmade Jewelry | Wholesale jewelry | Retail Jewelry sales at Festivals

Font styles to use
Script

Colors

Designer to choose colors to be used in the design.

Requirements
Must have
• A template that can be interchangable with the stone colors, names and healing properties.
Nice to have
• Some different ideas about the graphic color patterns on the card.
Should not have
• Any graphic that would cover the middle of the necklace card and keep people from seeing the neckalce

```html
<!DOCTYPE html>
<html lang="en">
<head>
<meta charset="utf-8">
<title>Brightwell Necklace Card – Pisces Fluorite</title>
<link rel="stylesheet" href="https://fonts.googleapis.com/css2?family=Quicksand:wght@500&family=Yellowtail&family=Pinyon+Script&display=swap">
<style>
  :root {
    --backdrop: #cbcbcb;
    --card: #ffffff;
    --ink-plum: #4b1a66;
    --bead-haze: #f1f0f3;
    --crystal-aqua: #9fe3ea;
    --crystal-blue: #5ea8e6;
    --crystal-violet: #a55bf0;
    --crystal-magenta: #e06fd0;
    --crystal-coral: #f2858f;
    --crystal-lilac: #d9b6f5;
  }
  html, body {
    margin: 0;
    padding: 0;
    width: 998px;
    height: 1200px;
    overflow: hidden;
    background: var(--backdrop);
  }
  .canvas {
    position: relative;
    width: 998px;
    height: 1200px;
  }
  .necklace-card {
    position: absolute;
    left: 278px;
    top: 282px;
    width: 474px;
    height: 632px;
    background: var(--card);
    overflow: hidden;
  }
  .necklace-photo {
    position: absolute;
    left: 0;
    top: 126px;
    width: 474px;
    height: 146px;
    background: linear-gradient(90deg,
      var(--bead-haze) 0%,
      #f3ece4 20%,
      #eadcec 40%,
      #e5d2ea 52%,
      #dfe3ea 68%,
      #e0eeee 85%,
      var(--bead-haze) 100%);
    clip-path: ellipse(62% 50% at 50% 45%);
  }
  .zodiac-symbol {
    position: absolute;
    left: 204px;
    top: 37px;
    width: 66px;
    height: 84px;
  }
  .zodiac-name {
    position: absolute;
    left: 0;
    top: 129px;
    width: 474px;
    text-align: center;
    margin: 0;
    font-family: "Quicksand", sans-serif;
    font-weight: 500;
    font-size: 22px;
    letter-spacing: 4px;
    color: var(--ink-plum);
  }
  .stone-name {
    position: absolute;
    left: 0;
    top: 264px;
    width: 474px;
    padding-left: 36px;
    box-sizing: border-box;
    text-align: center;
    margin: 0;
    font-family: "Yellowtail", cursive;
    font-weight: 400;
    font-size: 58px;
    line-height: 1.1;
    color: var(--ink-plum);
  }
  .healing-property {
    position: absolute;
    left: 0;
    top: 334px;
    width: 474px;
    padding-left: 14px;
    box-sizing: border-box;
    text-align: center;
    margin: 0;
    font-family: "Pinyon Script", cursive;
    font-size: 30px;
    line-height: 1.2;
    color: var(--ink-plum);
  }
  .crystal-graphic {
    position: absolute;
    left: 0;
    top: 404px;
    width: 474px;
    height: 228px;
    background:
      radial-gradient(circle at 8% 18%, var(--crystal-aqua) 0, transparent 32%),
      radial-gradient(circle at 22% 28%, var(--crystal-blue) 0, transparent 26%),
      radial-gradient(circle at 48% 80%, var(--crystal-coral) 0, transparent 30%),
      radial-gradient(circle at 58% 50%, var(--crystal-magenta) 0, transparent 30%),
      radial-gradient(circle at 85% 60%, var(--crystal-violet) 0, transparent 28%),
      radial-gradient(circle at 20% 75%, var(--crystal-violet) 0, transparent 26%),
      linear-gradient(120deg, var(--crystal-lilac), var(--crystal-magenta) 55%, var(--crystal-lilac));
    clip-path: polygon(0 7%, 48% 0, 100% 11%, 100% 100%, 0 100%);
  }
</style>
</head>
<body>
<main class="canvas">
  <article class="necklace-card">
    <div class="necklace-photo" role="img" aria-label="Photo of a fluorite bead necklace on a fine silver chain, faceted beads shading from clear and peach through purple to teal"></div>

    <svg class="zodiac-symbol" viewBox="0 0 66 84" aria-label="Pisces zodiac symbol" role="img">
      <path d="M3 0 C22 20 22 64 3 84" fill="none" stroke="var(--ink-plum)" stroke-width="4" stroke-linecap="round"/>
      <path d="M63 0 C44 20 44 64 63 84" fill="none" stroke="var(--ink-plum)" stroke-width="4" stroke-linecap="round"/>
      <path d="M0 42 L66 42" stroke="var(--ink-plum)" stroke-width="3.5" stroke-linecap="round"/>
    </svg>

    <p class="zodiac-name">Pisces</p>
    <h1 class="stone-name">Fluorite</h1>
    <p class="healing-property">Improves Decision Making</p>

    <div class="crystal-graphic" role="img" aria-label="Faceted crystal illustration in aqua, blue, violet, magenta and coral tones"></div>
  </article>
</main>
</body>
</html>
```